Culture Blueprint

I would like to edit the design of this culture blueprint graphic to align with my brand colors and services graphic. Please
The KITE stands for Leadership, Engagement, Activate Culture and Distinguish.
Work to be done:
1. Please make Purpose in red brand "kite" color
2. Please make Philosophy in grey brand "engage" color
3. Please make Priorities in and Processes (internal and external) in orange brand "active" color
4. Please make projections in teal "distinguish" color

Creativity welcomed!

```html
<!DOCTYPE html>
<html lang="en">
<head>
<meta charset="utf-8">
<title>Alignment of the Five Ps</title>
<link rel="stylesheet" href="https://fonts.googleapis.com/css2?family=Arimo:wght@700&family=Tinos:wght@700&display=swap">
<style>
  :root {
    --frame: #000000;
    --paper: #ffffff;
    --kite-red: #d42330;
    --engage-grey: #666666;
    --active-orange: #ef5f4f;
    --distinguish-teal: #0b8080;
    --arrow-grey: #a3a3a3;
    --ink: #000000;
    --label-light: #ffffff;
  }
  html, body {
    margin: 0;
    padding: 0;
    width: 1200px;
    height: 1200px;
    overflow: hidden;
    background: var(--frame);
  }
  .canvas {
    width: 1200px;
    height: 1200px;
    display: block;
  }
  .title {
    font-family: "Arimo", Arial, sans-serif;
    font-weight: 700;
    font-size: 20px;
    fill: var(--ink);
  }
  .ring-label {
    font-family: "Tinos", "Times New Roman", serif;
    font-weight: 700;
    font-size: 14px;
    fill: var(--label-light);
  }
  .core-label {
    font-family: "Tinos", "Times New Roman", serif;
    font-weight: 700;
    font-size: 18px;
    fill: var(--ink);
  }
  .callout {
    font-family: "Tinos", "Times New Roman", serif;
    font-weight: 700;
    font-size: 18px;
    fill: var(--ink);
  }
  .ring-teal { fill: var(--distinguish-teal); }
  .ring-orange { fill: var(--active-orange); }
  .ring-grey { fill: var(--engage-grey); }
  .ring-red { fill: var(--kite-red); }
  .dotted { fill: none; stroke: var(--ink); stroke-width: 1.2; stroke-dasharray: 2 2; }
  .divider { stroke: var(--ink); stroke-width: 1.4; }
  .spoke { stroke: var(--arrow-grey); stroke-width: 5; marker-start: url(#head); marker-end: url(#head); }
  .pointer { stroke: var(--ink); stroke-width: 2; marker-end: url(#pointer-head); }
</style>
</head>
<body>
<svg class="canvas" viewBox="0 0 1181 1181" width="1200" height="1200" xmlns="http://www.w3.org/2000/svg">
  <defs>
    <marker id="head" viewBox="0 0 10 10" refX="6" refY="5" markerWidth="3.2" markerHeight="3.2" orient="auto-start-reverse">
      <path d="M0,0 L10,5 L0,10 Z" fill="var(--arrow-grey)"/>
    </marker>
    <marker id="pointer-head" viewBox="0 0 10 10" refX="9" refY="5" markerWidth="5" markerHeight="5" orient="auto">
      <path d="M0,1 L10,5 L0,9 Z" fill="var(--ink)"/>
    </marker>
    <!-- clockwise circles start at bottom; counter-clockwise start at top -->
    <path id="cw-240" d="M572,827 A240,240 0 1 1 572,347 A240,240 0 1 1 572,827"/>
    <path id="ccw-253" d="M572,334 A253,253 0 1 0 572,840 A253,253 0 1 0 572,334"/>
    <path id="cw-196" d="M572,783 A196,196 0 1 1 572,391 A196,196 0 1 1 572,783"/>
    <path id="ccw-208" d="M572,379 A208,208 0 1 0 572,795 A208,208 0 1 0 572,379"/>
    <path id="cw-158" d="M572,745 A158,158 0 1 1 572,429 A158,158 0 1 1 572,745"/>
    <path id="cw-142" d="M572,729 A142,142 0 1 1 572,445 A142,142 0 1 1 572,729"/>
    <path id="cw-152" d="M572,739 A152,152 0 1 1 572,435 A152,152 0 1 1 572,739"/>
    <path id="ccw-148" d="M572,439 A148,148 0 1 0 572,735 A148,148 0 1 0 572,439"/>
    <path id="ccw-166" d="M572,421 A166,166 0 1 0 572,753 A166,166 0 1 0 572,421"/>
    <path id="ccw-157" d="M572,430 A157,157 0 1 0 572,744 A157,157 0 1 0 572,430"/>
    <path id="cw-102" d="M572,689 A102,102 0 1 1 572,485 A102,102 0 1 1 572,689"/>
    <path id="cw-57" d="M572,644 A57,57 0 1 1 572,530 A57,57 0 1 1 572,644"/>
  </defs>

  <rect class="paper" x="18" y="18" width="1145" height="1135" fill="var(--paper)"/>

  <text class="title" x="572" y="252" text-anchor="middle">Alignment of the Five Ps</text>

  <g class="blueprint">
    <!-- Projections -->
    <circle class="ring-teal" cx="572" cy="587" r="270"/>
    <circle class="dotted" cx="572" cy="587" r="270"/>
    <!-- External and internal practices -->
    <circle class="ring-orange" cx="572" cy="587" r="222"/>
    <circle class="dotted" cx="572" cy="587" r="222"/>
    <circle class="dotted" cx="572" cy="587" r="178"/>
    <circle class="dotted" cx="572" cy="587" r="131"/>
    <!-- Philosophy -->
    <circle class="ring-grey" cx="572" cy="587" r="85"/>
    <!-- Purpose -->
    <circle class="ring-red" cx="572" cy="587" r="43"/>
    <circle class="dotted" cx="572" cy="587" r="43"/>

    <g class="dividers projections">
      <line class="divider" x1="794" y1="587" x2="842" y2="587" transform="rotate(-112.5 572 587)"/>
      <line class="divider" x1="794" y1="587" x2="842" y2="587" transform="rotate(-67.5 572 587)"/>
      <line class="divider" x1="794" y1="587" x2="842" y2="587" transform="rotate(-22.5 572 587)"/>
      <line class="divider" x1="794" y1="587" x2="842" y2="587" transform="rotate(22.5 572 587)"/>
      <line class="divider" x1="794" y1="587" x2="842" y2="587" transform="rotate(67.5 572 587)"/>
      <line class="divider" x1="794" y1="587" x2="842" y2="587" transform="rotate(112.5 572 587)"/>
      <line class="divider" x1="794" y1="587" x2="842" y2="587" transform="rotate(157.5 572 587)"/>
      <line class="divider" x1="794" y1="587" x2="842" y2="587" transform="rotate(-157.5 572 587)"/>
    </g>
    <g class="dividers external">
      <line class="divider" x1="750" y1="587" x2="794" y2="587" transform="rotate(-125 572 587)"/>
      <line class="divider" x1="750" y1="587" x2="794" y2="587" transform="rotate(-55 572 587)"/>
      <line class="divider" x1="750" y1="587" x2="794" y2="587" transform="rotate(15 572 587)"/>
      <line class="divider" x1="750" y1="587" x2="794" y2="587" transform="rotate(62 572 587)"/>
      <line class="divider" x1="750" y1="587" x2="794" y2="587" transform="rotate(90 572 587)"/>
      <line class="divider" x1="750" y1="587" x2="794" y2="587" transform="rotate(118 572 587)"/>
      <line class="divider" x1="750" y1="587" x2="794" y2="587" transform="rotate(165 572 587)"/>
      <line class="divider" x1="750" y1="587" x2="794" y2="587" transform="rotate(180 572 587)"/>
    </g>
    <g class="dividers internal">
      <line class="divider" x1="703" y1="587" x2="750" y2="587" transform="rotate(-118 572 587)"/>
      <line class="divider" x1="703" y1="587" x2="750" y2="587" transform="rotate(-62 572 587)"/>
      <line class="divider" x1="703" y1="587" x2="750" y2="587"/>
      <line class="divider" x1="703" y1="587" x2="750" y2="587" transform="rotate(62 572 587)"/>
      <line class="divider" x1="703" y1="587" x2="750" y2="587" transform="rotate(118 572 587)"/>
      <line class="divider" x1="703" y1="587" x2="750" y2="587" transform="rotate(180 572 587)"/>
    </g>

    <g class="spokes">
      <line class="spoke" x1="622" y1="587" x2="790" y2="587" transform="rotate(-86 572 587)"/>
      <line class="spoke" x1="622" y1="587" x2="744" y2="587" transform="rotate(-76 572 587)"/>
      <line class="spoke" x1="622" y1="587" x2="800" y2="587" transform="rotate(-50 572 587)"/>
      <line class="spoke" x1="622" y1="587" x2="700" y2="587" transform="rotate(-32 572 587)"/>
      <line class="spoke" x1="622" y1="587" x2="744" y2="587" transform="rotate(-18 572 587)"/>
      <line class="spoke" x1="622" y1="587" x2="700" y2="587" transform="rotate(-8 572 587)"/>
      <line class="spoke" x1="622" y1="587" x2="800" y2="587"/>
      <line class="spoke" x1="622" y1="587" x2="700" y2="587" transform="rotate(28 572 587)"/>
      <line class="spoke" x1="622" y1="587" x2="800" y2="587" transform="rotate(46 572 587)"/>
      <line class="spoke" x1="622" y1="587" x2="744" y2="587" transform="rotate(56 572 587)"/>
      <line class="spoke" x1="622" y1="587" x2="700" y2="587" transform="rotate(78 572 587)"/>
      <line class="spoke" x1="622" y1="587" x2="800" y2="587" transform="rotate(90 572 587)"/>
      <line class="spoke" x1="622" y1="587" x2="744" y2="587" transform="rotate(98 572 587)"/>
      <line class="spoke" x1="622" y1="587" x2="744" y2="587" transform="rotate(120 572 587)"/>
      <line class="spoke" x1="622" y1="587" x2="800" y2="587" transform="rotate(132 572 587)"/>
      <line class="spoke" x1="622" y1="587" x2="700" y2="587" transform="rotate(150 572 587)"/>
      <line class="spoke" x1="622" y1="587" x2="800" y2="587" transform="rotate(180 572 587)"/>
      <line class="spoke" x1="622" y1="587" x2="700" y2="587" transform="rotate(-165 572 587)"/>
      <line class="spoke" x1="622" y1="587" x2="744" y2="587" transform="rotate(-158 572 587)"/>
      <line class="spoke" x1="622" y1="587" x2="700" y2="587" transform="rotate(-145 572 587)"/>
      <line class="spoke" x1="622" y1="587" x2="800" y2="587" transform="rotate(-117 572 587)"/>
    </g>

    <g class="labels projections">
      <text class="ring-label"><textPath href="#cw-240" startOffset="50%" text-anchor="middle">Name</textPath></text>
      <text class="ring-label"><textPath href="#cw-240" startOffset="62.5%" text-anchor="middle">Logo/Symbols</textPath></text>
      <text class="ring-label"><textPath href="#cw-240" startOffset="75%" text-anchor="middle">Headquarters</textPath></text>
      <text class="ring-label"><textPath href="#ccw-253" startOffset="62.5%" text-anchor="middle">Leader Image</textPath></text>
      <text class="ring-label"><textPath href="#ccw-253" startOffset="50%" text-anchor="middle">Offices/Storese</textPath></text>
      <text class="ring-label"><textPath href="#ccw-253" startOffset="37.5%" text-anchor="middle">Dress/Uniforms</textPath></text>
      <text class="ring-label"><textPath href="#cw-240" startOffset="25%" text-anchor="middle">Marketing/PR/Advertising</textPath></text>
      <text class="ring-label"><textPath href="#cw-240" startOffset="37.5%" text-anchor="middle">Community Activities</textPath></text>
    </g>

    <g class="labels external">
      <text class="ring-label"><textPath href="#cw-196" startOffset="50%" text-anchor="middle">Customers</textPath></text>
      <text class="ring-label"><textPath href="#cw-196" startOffset="69.2%" text-anchor="middle">Markets</textPath></text>
      <text class="ring-label"><textPath href="#ccw-208" startOffset="59.4%" text-anchor="middle">Products</textPath></text>
      <text class="ring-label"><textPath href="#ccw-208" startOffset="39.2%" text-anchor="middle">Services</textPath></text>
      <text class="ring-label"><textPath href="#cw-196" startOffset="31.9%" text-anchor="middle">Suppliers/Vendors &amp; Partners</textPath></text>
    </g>

    <g class="labels internal">
      <text class="ring-label"><textPath href="#cw-158" startOffset="50%" text-anchor="middle">Structure, Work</textPath></text>
      <text class="ring-label"><textPath href="#cw-142" startOffset="50%" text-anchor="middle">Design &amp; Systems</textPath></text>
      <text class="ring-label"><textPath href="#cw-158" startOffset="65.3%" text-anchor="middle">Recruitment</textPath></text>
      <text class="ring-label"><textPath href="#cw-142" startOffset="65.3%" text-anchor="middle">&amp; Selection</textPath></text>
      <text class="ring-label"><textPath href="#ccw-148" startOffset="66.7%" text-anchor="middle">Training &amp;</textPath></text>
      <text class="ring-label"><textPath href="#ccw-166" startOffset="66.7%" text-anchor="middle">Developement</textPath></text>
      <text class="ring-label"><textPath href="#ccw-148" startOffset="50%" text-anchor="middle">Performance</textPath></text>
      <text class="ring-label"><textPath href="#ccw-166" startOffset="50%" text-anchor="middle">Management</textPath></text>
      <text class="ring-label"><textPath href="#ccw-148" startOffset="34.7%" text-anchor="middle">Internal</textPath></text>
      <text class="ring-label"><textPath href="#ccw-166" startOffset="34.7%" text-anchor="middle">Communications</textPath></text>
      <text class="ring-label"><textPath href="#cw-152" startOffset="33.3%" text-anchor="middle">Technology</textPath></text>
    </g>

    <g class="labels core">
      <text class="core-label"><textPath href="#cw-102" startOffset="50%" text-anchor="middle">Priorities</textPath></text>
      <text class="core-label"><textPath href="#cw-57" startOffset="50%" text-anchor="middle">Philosophy</textPath></text>
      <text class="core-label" x="573" y="593" text-anchor="middle">Purpose</text>
    </g>
  </g>

  <g class="callouts">
    <line class="pointer" x1="843" y1="393" x2="755" y2="393"/>
    <text class="callout" x="849" y="400">Projections</text>

    <line class="pointer" x1="858" y1="464" x2="752" y2="464"/>
    <text class="callout" x="864" y="471">External</text>
    <text class="callout" x="864" y="494">Practices</text>

    <line class="pointer" x1="860" y1="556" x2="742" y2="556"/>
    <text class="callout" x="866" y="563">Internal</text>
    <text class="callout" x="866" y="586">Practices</text>

    <line class="pointer" x1="878" y1="628" x2="710" y2="599"/>
    <text class="callout" x="883" y="635">Core</text>
    <text class="callout" x="873" y="658">Culture</text>
  </g>
</svg>
</body>
</html>
```